Business Card Design Project

Use our current logo. Clean design.

Industry/Entity Type

Business

Requirements
Must have
• Marisela DUBRANCQ
M. Law
Managing Partner

Alpenvorsa AG
Kornhalmweg 214
CH-3097 Liebefeld

M. +41 79 412 56 27
T. +41 31 928 44 10
F. +41 31 928 44 19

m.dubrancq@alpenvorsa-example.com
www.alpenvorsa-example.com

```html
<!DOCTYPE html>
<html lang="en">
<head>
<meta charset="utf-8">
<title>Alpenvorsa AG – Business Card</title>
<link href="https://fonts.googleapis.com/css2?family=Questrial&display=swap" rel="stylesheet">
<style>
  :root {
    --stage: #e9e7e3;
    --paper: #ffffff;
    --paper-shade: #dcdcdc;
    --ink: #1c1c1c;
    --ink-soft: #3a3a3a;
    --night: #141414;
    --night-glow: #3a3a3a;
    --night-ink: #f2f2f2;
  }
  * { box-sizing: border-box; margin: 0; padding: 0; }
  html, body {
    width: 1200px; height: 900px; overflow: hidden;
    background: var(--stage);
    font-family: "Questrial", "Helvetica Neue", Arial, sans-serif;
  }
  .canvas {
    width: 1200px; height: 900px;
    display: flex; align-items: center; justify-content: center; gap: 40px;
  }
  .card {
    position: relative;
    width: 540px; height: 310px;
    border-radius: 4px;
    box-shadow: 0 10px 28px rgba(0,0,0,.18), 0 2px 6px rgba(0,0,0,.12);
  }
  /* Front */
  .card--front {
    background: radial-gradient(ellipse at 60% 45%, var(--paper) 35%, var(--paper-shade) 100%);
    border-top-left-radius: 46px;
    color: var(--ink);
  }
  .brand {
    position: absolute; left: 34px; top: 34px;
    display: flex; align-items: center; gap: 8px;
  }
  .brand__mark { width: 10px; height: 10px; background: var(--ink); }
  .brand__name { font-size: 17px; letter-spacing: 2px; color: var(--ink); }
  .holder { position: absolute; left: 34px; top: 118px; font-size: 11px; line-height: 1.45; }
  .address { position: absolute; left: 34px; top: 200px; font-size: 11px; line-height: 1.45; color: var(--ink-soft); }
  .contacts {
    position: absolute; right: 30px; top: 34px;
    list-style: none; font-size: 10.5px; line-height: 1;
  }
  .contacts li {
    display: flex; justify-content: flex-end; align-items: center; gap: 9px;
    height: 21px;
  }
  .contacts svg { width: 11px; height: 11px; fill: none; stroke: var(--ink); stroke-width: 1.6; flex: none; }
  /* Back */
  .card--back {
    background: radial-gradient(circle at 68% 72%, var(--night-glow) 0%, var(--night) 42%);
    border-bottom-right-radius: 46px;
    color: var(--night-ink);
  }
  .back__url { position: absolute; left: 46px; top: 56px; font-size: 12px; letter-spacing: .5px; }
  .back__brand {
    position: absolute; right: 52px; bottom: 62px;
    display: flex; align-items: center; gap: 10px;
  }
  .back__brand .brand__mark { background: var(--night-ink); width: 12px; height: 12px; }
  .back__brand .brand__name { color: var(--night-ink); font-size: 22px; letter-spacing: 3px; }
</style>
</head>
<body>
<main class="canvas">
  <section class="card card--front" aria-label="Business card front">
    <div class="brand">
      <span class="brand__mark"></span>
      <span class="brand__name">ALPENVORSA</span>
    </div>
    <div class="holder">
      <p>Marisela DUBRANCQ M.Law</p>
      <p>Managing Partner</p>
    </div>
    <div class="address">
      <p>Alpenvorsa AG</p>
      <p>Kornhalmweg 214</p>
      <p>CH-3097 Liebefeld</p>
    </div>
    <ul class="contacts">
      <li>+41 79 412 56 27
        <svg viewBox="0 0 12 12" aria-hidden="true"><rect x="3" y="1" width="6" height="10" rx="1"/><line x1="5" y1="9" x2="7" y2="9"/></svg></li>
      <li>+41 31 928 44 10
        <svg viewBox="0 0 12 12" aria-hidden="true"><path d="M2 1.5 L4.5 1.5 L5.5 4 L4 5 Q5 7.5 7 8 L8 6.5 L10.5 7.5 L10.5 10 Q5 10.5 1.5 4 Z"/></svg></li>
      <li>+41 31 928 44 19
        <svg viewBox="0 0 12 12" aria-hidden="true"><rect x="3" y="1" width="6" height="3"/><rect x="1" y="4" width="10" height="5"/><rect x="3" y="8" width="6" height="3"/></svg></li>
      <li>m.dubrancq@alpenvorsa-example.com
        <svg viewBox="0 0 12 12" aria-hidden="true"><rect x="1" y="2.5" width="10" height="7"/><path d="M1 2.5 L6 6.5 L11 2.5"/></svg></li>
      <li>www.alpenvorsa-example.com
        <svg viewBox="0 0 12 12" aria-hidden="true"><circle cx="6" cy="6" r="4.8"/><line x1="1.2" y1="6" x2="10.8" y2="6"/><ellipse cx="6" cy="6" rx="2" ry="4.8"/></svg></li>
    </ul>
  </section>

  <section class="card card--back" aria-label="Business card back">
    <p class="back__url">www.alpenvorsa-example.com</p>
    <div class="back__brand">
      <span class="brand__mark"></span>
      <span class="brand__name">ALPENVORSA</span>
    </div>
  </section>
</main>
</body>
</html>
```